Wordpress Design for a Private Label BBQ Brand

For our new brand, we'd need a new Wordpress website. We'd prefer to run the website on Wordpress

We'd like to include the following
- space for description of the brand
- space for product portfolio (not a shop!)
- space for socials
- space for support
- space for contact

```html
<!DOCTYPE html>
<html lang="en">
<head>
<meta charset="utf-8">
<title>Bracero — BBQ</title>
<link rel="stylesheet" href="https://fonts.googleapis.com/css2?family=Playfair+Display:wght@700;900&family=Poppins:wght@400;500;600;700&display=swap">
<style>
:root{
  --red:#d42a1c;
  --orange:#e8561f;
  --ink:#0b0b0b;
  --text:#3a3a3a;
  --blush:#fce9e4;
  --faint:#f0f0f0;
  --white:#ffffff;
  --grey:#c9c9c9;
}
*{margin:0;padding:0;box-sizing:border-box}
html,body{width:1200px;height:3316px;overflow:hidden;background:var(--white)}
body{position:relative;font-family:'Poppins',sans-serif;color:var(--text)}
.abs{position:absolute}
.serif{font-family:'Playfair Display',serif;font-weight:900;color:var(--ink)}
.brand{display:flex;align-items:center;gap:10px;font-family:'Playfair Display',serif;font-weight:700;color:var(--ink)}
.brand .dot{width:22px;height:22px;border-radius:50%;background:var(--red)}
.nav{top:30px;left:568px;display:flex;gap:26px;align-items:center;font-size:15px;font-weight:600;color:var(--ink)}
.nav .home{width:14px;height:14px}
.btn-outline{display:flex;align-items:center;justify-content:center;gap:10px;border:2px solid var(--red);border-radius:30px;font-weight:500;color:var(--ink);font-size:16px;background:transparent}
.btn-solid{display:flex;align-items:center;justify-content:center;gap:10px;border-radius:30px;background:linear-gradient(90deg,var(--red),var(--orange));color:var(--white);font-weight:700;font-size:14px}
.kicker{color:var(--red);font-family:'Playfair Display',serif;font-weight:900}
.center{left:0;width:1200px;text-align:center}
.para{font-size:16px;line-height:26px}
.ph{border-radius:12px}
.card{background:var(--white);border-radius:10px;box-shadow:0 6px 24px rgba(0,0,0,.10)}
.card .mini{position:absolute;right:22px;bottom:22px;font-family:'Playfair Display',serif;font-weight:700;font-size:11px;color:var(--ink)}
.dots span{display:inline-block;width:13px;height:13px;border-radius:50%;background:var(--grey);margin-right:7px}
.dots span.on{background:var(--red)}
.newsletter{left:167px;top:2659px;width:866px;height:170px;border-radius:85px;background:linear-gradient(90deg,#c9221c,#e5461d 60%,#ec5a1e)}
.field{left:570px;top:2722px;width:405px;height:49px;border-radius:25px;background:var(--white);font-size:13px;color:#555;padding-left:28px;display:flex;align-items:center}
.subscribe{left:822px;top:2722px;width:153px;height:49px;border-radius:25px;background:var(--ink);color:var(--white);font-weight:700;font-size:13px;display:flex;align-items:center;justify-content:center}
.footer-h{font-size:18px;font-weight:700;color:var(--white)}
.links li{list-style:none;font-size:14px;color:var(--white);height:25px}
.contact li{list-style:none;font-size:14px;color:var(--white);height:25px;display:flex;align-items:center;gap:8px}
.contact svg{width:12px;height:12px}
.social{width:34px;height:34px;border-radius:50%;background:#1c1c1c;border:1px solid #333}
</style>
</head>
<body>

<svg class="abs" style="left:0;top:0" width="1200" height="3316" aria-hidden="true">
  <path d="M0 880 C120 720 320 660 520 690 C700 720 850 760 1000 720 C1110 690 1170 640 1200 592 L1200 1040 C1100 1150 900 1230 700 1250 C600 1300 480 1500 300 1500 C120 1500 20 1400 0 1320 Z" fill="var(--blush)"/>
  <path d="M0 3050 C150 2870 400 2830 700 2870 C950 2900 1100 2860 1200 2755 L1200 3316 L0 3316 Z" fill="var(--ink)"/>
</svg>

<header>
  <div class="abs brand" style="left:88px;top:14px;font-size:33px"><span class="dot"></span>BRACERO</div>
  <nav class="abs nav">
    <svg class="home" viewBox="0 0 14 14"><path d="M7 1 L13 7 H11 V13 H3 V7 H1 Z" fill="var(--red)"/></svg>
    <span>About</span><span>Product portfolio</span><span>Socials</span><span>Support</span>
  </nav>
  <div class="abs btn-outline" style="left:993px;top:21px;width:117px;height:43px;font-weight:600;font-size:15px">Contact</div>
</header>

<section class="hero">
  <div class="abs center kicker" style="top:124px;font-size:36px">WELCOME TO</div>
  <div class="abs center serif" style="top:160px;font-size:100px;line-height:110px;letter-spacing:1px">BRACERO</div>
  <p class="abs center para" style="top:270px;font-size:16px">Lorem Ipsum is simply dummy text of the printing and typesetting industry. Lorem Ipsum<br>has been the industry's standard dummy text ever since.</p>
  <div class="abs btn-solid" style="left:516px;top:335px;width:166px;height:47px">CONTACT US <span>→</span></div>
  <div class="abs ph" role="img" aria-label="Three black ceramic kamado grills" style="left:238px;top:393px;width:689px;height:405px;background:radial-gradient(ellipse at center,#3a3a3a 0%,#1a1a1a 55%,rgba(255,255,255,0) 72%)"></div>
</section>

<section class="about">
  <div class="abs" role="img" aria-label="Close-up of kamado grill vent in front of an orange flame" style="left:0;top:798px;width:521px;height:513px;background:linear-gradient(160deg,#e8561f 0%,#d42a1c 35%,#2a2a2a 60%,#1a1a1a 100%);border-radius:0 40px 0 0"></div>
  <div class="abs serif" style="left:564px;top:852px;font-size:49px">ABOUT US</div>
  <p class="abs para" style="left:564px;top:918px;width:530px">Lorem Ipsum is simply dummy text of the printing and typesetting industry. Lorem Ipsum has been the industry's standard dummy text ever since the 1500s, when an unknown printer took a galley of type and scrambled it to make a type specimen book. It has survived not only five centuries, but also the leap into electronic typesetting, remaining essentially unchanged.</p>
  <div class="abs btn-outline" style="left:564px;top:1091px;width:164px;height:51px">READ MORE <span>→</span></div>
  <div class="abs" role="img" aria-label="Stainless steel grill fork" style="left:979px;top:959px;width:221px;height:206px;background:linear-gradient(140deg,rgba(0,0,0,0) 40%,#222 48%,#9a9a9a 60%,rgba(0,0,0,0) 70%)"></div>
</section>

<section class="portfolio">
  <div class="abs center kicker" style="top:1530px;font-size:26px">PRODUCT</div>
  <div class="abs center serif" style="top:1552px;font-size:49px">PORTFOLIO</div>

  <div class="abs card" style="left:89px;top:1646px;width:263px;height:321px">
    <div class="abs ph" role="img" aria-label="Kamado grill with open lid" style="left:40px;top:75px;width:170px;height:150px;background:radial-gradient(circle,#e8e2d4 0%,#2a2a2a 65%,rgba(255,255,255,0) 72%)"></div>
    <div class="mini">BRACERO</div>
  </div>
  <div class="abs card" style="left:363px;top:1646px;width:263px;height:321px">
    <div class="abs ph" role="img" aria-label="Barbecue tool set in case" style="left:42px;top:72px;width:176px;height:125px;background:linear-gradient(180deg,#bfbfbf,#1e1e1e 20%,#4a4a4a 60%,#1e1e1e)"></div>
    <div class="mini">BRACERO</div>
  </div>
  <div class="abs card" style="left:639px;top:1646px;width:471px;height:321px">
    <div class="abs ph" role="img" aria-label="Pair of grill lifting tools" style="left:140px;top:60px;width:190px;height:200px;background:linear-gradient(90deg,rgba(255,255,255,0) 8%,#6b6b6b 18%,#1e1e1e 28%,rgba(255,255,255,0) 38%,rgba(255,255,255,0) 62%,#6b6b6b 72%,#1e1e1e 82%,rgba(255,255,255,0) 92%)"></div>
    <div class="mini" style="font-size:14px;right:24px;bottom:20px">BRACERO</div>
  </div>
  <div class="abs dots" style="left:573px;top:2012px"><span class="on"></span><span></span><span></span></div>
</section>

<section class="support">
  <div class="abs serif" style="left:84px;top:2193px;font-size:80px;color:var(--faint)">BRACERO</div>
  <div class="abs serif" style="left:84px;top:2272px;font-size:49px">SUPPORT 24/7</div>
  <p class="abs para" style="left:84px;top:2338px;width:530px">Lorem Ipsum is simply dummy text of the printing and typesetting industry. Lorem Ipsum has been the industry's standard dummy text ever since the 1500s, when an unknown printer took a galley of type and scrambled it to make a type specimen book.</p>
  <div class="abs btn-outline" style="left:84px;top:2456px;width:162px;height:51px">CONTACT US <span>→</span></div>
  <div class="abs" role="img" aria-label="Thoughtful man framed by red and orange flames" style="left:663px;top:2054px;width:434px;height:560px;background:linear-gradient(160deg,#d42a1c 0%,#e8561f 45%,#7a4a38 75%,#5a3a2a 100%);border-radius:60% 40% 45% 55% / 55% 45% 40% 45%"></div>
</section>

<section class="abs newsletter">
  <div class="abs serif" style="left:84px;top:46px;font-size:40px;color:var(--white)">NEWSLETTER</div>
  <div class="abs" style="left:84px;top:96px;font-size:15px;color:var(--white)">Subscribe to our newsletter</div>
</section>
<div class="abs field">Enter your email</div>
<div class="abs subscribe">SUBSCRIBE</div>

<footer>
  <div class="abs brand" style="left:122px;top:3050px;font-size:38px;color:var(--white)"><span class="dot" style="width:26px;height:26px"></span>BRACERO</div>
  <div class="abs footer-h" style="left:431px;top:2978px">Useful Links</div>
  <ul class="abs links" style="left:431px;top:3012px">
    <li>Home</li><li>About</li><li>Product portfolio</li><li>Socials</li><li>Support</li><li>Contact Us</li>
  </ul>
  <div class="abs footer-h" style="left:670px;top:2978px">Contact Us</div>
  <ul class="abs contact" style="left:670px;top:3012px">
    <li><svg viewBox="0 0 12 12"><path d="M6 0 A4 4 0 0 1 10 4 C10 7 6 12 6 12 C6 12 2 7 2 4 A4 4 0 0 1 6 0 Z" fill="var(--red)"/></svg>Some goes address here</li>
    <li><svg viewBox="0 0 12 12"><rect x="0" y="2" width="12" height="8" fill="var(--red)"/><path d="M0 2 L6 7 L12 2" stroke="#fff" fill="none"/></svg>info@email.com</li>
    <li><svg viewBox="0 0 12 12"><path d="M2 0 L5 3 L3.5 5 C4.5 7 5 7.5 7 8.5 L9 7 L12 10 L10 12 C5 11 1 7 0 2 Z" fill="var(--red)"/></svg>+1555 010 2030</li>
    <li><svg viewBox="0 0 12 12"><rect x="1" y="4" width="10" height="6" fill="var(--red)"/><rect x="3" y="1" width="6" height="3" fill="var(--red)"/></svg>1555 010 2031</li>
  </ul>
  <div class="abs social" aria-label="Social profile" style="left:920px;top:3047px"></div>
  <div class="abs social" aria-label="Social profile" style="left:962px;top:3047px"></div>
  <div class="abs social" aria-label="Social profile" style="left:1004px;top:3047px"></div>
  <div class="abs social" aria-label="Social profile" style="left:1045px;top:3047px"></div>
  <div class="abs" style="left:89px;top:3255px;width:1021px;height:1px;background:#333"></div>
  <div class="abs center" style="top:3275px;font-size:14px;color:var(--white)">©Copyright 2023 | All Rights Reserved</div>
  <div class="abs" style="left:1120px;top:3232px;width:40px;height:40px;border-radius:50%;background:var(--red);color:var(--white);font-size:14px;display:flex;align-items:center;justify-content:center">˄</div>
</footer>

</body>
</html>
```